Business card design for Automotive workshop

We need a business card for a new automotive repair and tyre shop called Ridgeback Prime Automotive located in New Zealand. We are a clean, modern and fresh workshop and company.

Front needs to feature logo,
my name:
Lachie Westergaard (director)

Address:
48 Marlow Lane
Whitianga 3510

Phone: 07 842 1937
Mobile: 027 519 2764
Email: office@ridgebackmotors.co.nz
Website: ridgebackmotors.co.nz

Back needs to feature an area to write down appointment details, date and time.

Also feature a list of jobs and work we do such as,
Vehicle Servicing
All Mechanical Repairs
Warrant of Fitness
Tyres & Wheel Alignments
Automotive Diagnostics
Automotive Parts & Supplies

```html
<!DOCTYPE html>
<html lang="en">
<head>
<meta charset="utf-8">
<title>Ridgeback Prime Automotive – Business Card</title>
<link rel="stylesheet" href="https://fonts.googleapis.com/css2?family=Exo+2:wght@400;500;600;700&display=swap">
<style>
  :root {
    --page-bg: #2b2e33;
    --card-bg: #121213;
    --panel-grey: #333335;
    --brand-red: #e31e26;
    --text-white: #ffffff;
    --text-soft: #e6e6e6;
    --dash: #bdbdbd;
  }
  * { box-sizing: border-box; margin: 0; padding: 0; }
  html, body {
    width: 1200px; height: 1000px; overflow: hidden;
    background: var(--page-bg);
    font-family: "Exo 2", sans-serif;
    color: var(--text-white);
  }
  .card {
    position: absolute; left: 220px;
    width: 760px; height: 434px;
    background: var(--card-bg);
    border-radius: 22px; overflow: hidden;
    box-shadow: 0 14px 30px rgba(0,0,0,.45);
  }
  .card--back { top: 36px; }
  .card--front { top: 520px; }

  /* Back side */
  .back-brand {
    position: absolute; left: 50px; top: 24px; bottom: 24px;
    writing-mode: vertical-rl; transform: rotate(180deg);
    display: flex; align-items: center; justify-content: center; gap: 10px;
    font-weight: 700; font-size: 20px; letter-spacing: 1px;
    text-transform: uppercase; white-space: nowrap;
  }
  .brand-square { width: 14px; height: 14px; background: var(--brand-red); flex: none; }
  .field {
    position: absolute; display: flex; align-items: baseline;
    font-weight: 700; font-size: 19px;
  }
  .field__line { flex: 1; border-bottom: 2px dashed var(--dash); margin-left: 8px; height: 1px; }
  .field--date { left: 230px; top: 60px; width: 260px; }
  .field--time { left: 515px; top: 60px; width: 210px; }
  .appointment-label { position: absolute; left: 200px; top: 108px; font-weight: 700; font-size: 19px; }
  .appointment-box {
    position: absolute; left: 200px; top: 140px;
    width: 525px; height: 140px; background: var(--panel-grey);
  }
  .service-list { position: absolute; list-style: none; font-size: 17px; font-weight: 500; line-height: 27px; }
  .service-list li::before {
    content: ""; display: inline-block; width: 7px; height: 7px; border-radius: 50%;
    background: var(--brand-red); margin-right: 8px; vertical-align: 5px;
  }
  .service-list--left { left: 170px; top: 300px; }
  .service-list--right { left: 470px; top: 327px; }

  /* Front side */
  .front-brand {
    position: absolute; left: 0; right: 0; top: 78px;
    display: flex; align-items: center; justify-content: center; gap: 14px;
    font-weight: 700; font-size: 34px; letter-spacing: 2px; text-transform: uppercase;
  }
  .front-brand .brand-square { width: 18px; height: 18px; }
  .person { position: absolute; right: 440px; top: 222px; text-align: right; }
  .person__name { color: var(--brand-red); font-weight: 700; font-size: 30px; white-space: nowrap; }
  .person__role { font-size: 19px; font-weight: 500; margin-top: 6px; }
  .divider { position: absolute; left: 345px; top: 218px; width: 2px; height: 112px; background: var(--text-soft); }
  .contact-list { position: absolute; left: 368px; top: 214px; list-style: none; font-size: 19px; font-weight: 500; line-height: 29px; }
  .contact-list li { display: flex; align-items: center; gap: 10px; white-space: nowrap; }
  .contact-list svg { width: 14px; height: 14px; flex: none; }
  .address-band {
    position: absolute; left: 0; right: 0; top: 356px; height: 48px;
    background: var(--brand-red);
    display: flex; align-items: center; padding-left: 240px;
    font-size: 19px; font-weight: 500;
  }
</style>
</head>
<body>

<section class="card card--back" aria-label="Card back">
  <div class="back-brand"><span class="brand-square"></span>Ridgeback Prime Automotive</div>

  <div class="field field--date">Date<span class="field__line"></span></div>
  <div class="field field--time">Time<span class="field__line"></span></div>
  <p class="appointment-label">Appointment Details</p>
  <div class="appointment-box"></div>

  <ul class="service-list service-list--left">
    <li>Vehicle Servicing</li>
    <li>Automotive Diagnostics</li>
    <li>Tyres &amp; Wheel Alignments</li>
  </ul>
  <ul class="service-list service-list--right">
    <li>Warrant of Fitness</li>
    <li>All Mechanical Repairs</li>
    <li>Automotive Parts &amp; Supplies</li>
  </ul>
</section>

<section class="card card--front" aria-label="Card front">
  <div class="front-brand"><span class="brand-square"></span>Ridgeback Prime Automotive</div>

  <div class="person">
    <p class="person__name">Lachie Westergaard</p>
    <p class="person__role">Director</p>
  </div>
  <div class="divider"></div>

  <ul class="contact-list">
    <li>
      <svg viewBox="0 0 24 24" fill="#e31e26" aria-hidden="true"><path d="M6.6 10.8a15 15 0 0 0 6.6 6.6l2.2-2.2a1 1 0 0 1 1-.25 11.4 11.4 0 0 0 3.6.57 1 1 0 0 1 1 1V20a1 1 0 0 1-1 1A17 17 0 0 1 3 4a1 1 0 0 1 1-1h3.5a1 1 0 0 1 1 1c0 1.25.2 2.45.57 3.57a1 1 0 0 1-.25 1z"/></svg>
      07 842 1937
    </li>
    <li>
      <svg viewBox="0 0 24 24" fill="none" stroke="#e31e26" stroke-width="2.4" aria-hidden="true"><rect x="6" y="2" width="12" height="20" rx="2"/><line x1="11" y1="18" x2="13" y2="18"/></svg>
      027 519 2764
    </li>
    <li>
      <svg viewBox="0 0 24 24" fill="none" stroke="#e31e26" stroke-width="2.4" aria-hidden="true"><rect x="2" y="5" width="20" height="14" rx="1"/><polyline points="2,5 12,13 22,5"/></svg>
      office@ridgebackmotors.co.nz
    </li>
    <li>
      <svg viewBox="0 0 24 24" fill="none" stroke="#e31e26" stroke-width="2.2" aria-hidden="true"><circle cx="12" cy="12" r="10"/><ellipse cx="12" cy="12" rx="4" ry="10"/><line x1="2" y1="12" x2="22" y2="12"/></svg>
      ridgebackmotors.co.nz
    </li>
  </ul>

  <div class="address-band">48 Marlow Lane Whitianga 3510</div>
</section>

</body>
</html>
```